Brightleaf Rx Pass reinvent our website.

Our Website is outdated and needs an overhaul, in every aspect. We assist individuals that have little or no prescription coverage and allow them to receive a discount ranging from 33% up to 78% for free. In the beginning we utilized pharmacies to spread the word, but times have a changed. We are looking for a modern and clean site. We are open to anything, image, logo etc.

Tallon Market Market(s)

Anyone regardless of residency, age or income. This program is designed to assist those that have NO prescription coverage or for those whose particular prescription may not be covered by insurance.

Industry/Entity Type

Pharmaceutical

Coding

Coded - Design and coding required

Number of Pages Required

4 page

Requirements
Must have
• -The two MUST haves are the pharmacy locators & drug pricing. If you can combine the 2, even better.
• -a ongoing counter/tally on the 1stpage reflecting the amount of money we are saving customers. http://plumtorvex.net/item/tally-widgets-v-20-motion-pack/full_screen_preview/58203946
• -on a smart phone the ability to view the information that is needed to get the actual discount for the medication.
Nice to have
• animated tutorial showing how to use the card
• health blog

```html
<!DOCTYPE html>
<html lang="en">
<head>
<meta charset="utf-8">
<title>Brightleaf Rx Pass – Free Prescription Assistance Program</title>
<link rel="stylesheet" href="https://fonts.googleapis.com/css2?family=Josefin+Sans:wght@400;600;700&family=Lato:ital,wght@0,300;0,400;0,700;1,400&display=swap">
<style>
:root{
  --teal:#2a9bb0;
  --teal-light:#7fc8d8;
  --teal-pale:#c9e7ee;
  --footer:#3aa6b9;
  --orange:#f26522;
  --ink:#1f2a30;
  --slate:#5f6d73;
  --grey:#8b969b;
  --rule:#d9dee0;
  --white:#ffffff;
}
*{box-sizing:border-box;margin:0;padding:0}
html,body{width:1200px;height:3291px;overflow:hidden;background:var(--white)}
body{position:relative;font-family:'Lato',sans-serif;color:var(--ink)}
.abs{position:absolute}
.deco{position:absolute;border-radius:40px;background:linear-gradient(90deg,var(--teal-light),var(--teal-pale))}

/* nav */
.site-nav{position:absolute;top:62px;left:484px;display:flex;gap:0;font-family:'Josefin Sans',sans-serif;font-weight:700;font-size:13px;letter-spacing:.3px;color:var(--ink)}
.site-nav a{color:inherit;text-decoration:none;margin-right:42px}

/* hero */
.brand-dot{left:578px;top:232px;width:44px;height:32px;border-radius:50%;background:var(--teal)}
.hero-title{top:292px;left:0;width:1200px;text-align:center;font-family:'Josefin Sans',sans-serif;font-weight:700;font-size:46px;letter-spacing:1px;color:var(--ink)}
.hero-sub{top:362px;left:0;width:1200px;text-align:center;font-family:'Lato',sans-serif;font-weight:700;font-size:34px;color:var(--teal)}
.btn{display:block;position:absolute;width:172px;height:36px;line-height:37px;text-align:center;background:var(--orange);color:var(--white);font-family:'Lato',sans-serif;font-weight:700;font-size:15px;text-decoration:none;left:514px}

.divider{position:absolute;left:599px;width:3px;background:var(--teal-light)}
.divider::before,.divider::after{content:"";position:absolute;top:-2px;width:22px;height:3px;background:var(--teal-light)}
.divider::before{right:0;transform-origin:right;transform:rotate(35deg)}
.divider::after{left:0;transform-origin:left;transform:rotate(-35deg)}

.section-title{position:absolute;left:0;width:1200px;text-align:center;font-family:'Lato',sans-serif;font-weight:700;font-size:40px;color:var(--slate)}
.section-title span{display:inline-block;border-bottom:3px solid var(--teal-light);padding:0 4px 4px}

.mission-lead{top:830px;left:305px;width:590px;text-align:center;font-size:17px;line-height:23px;color:var(--teal)}
.mission-body{top:950px;left:295px;width:610px;text-align:center;font-size:22px;line-height:25px;color:var(--slate)}

/* steps */
.step-art{position:absolute;border-radius:8px;background:linear-gradient(180deg,var(--teal),#3fb0c3)}
.step-label{position:absolute;top:1614px;width:340px;text-align:center;font-weight:700;font-size:21px;color:var(--teal-light)}

/* savings */
.savings-title{top:1744px;left:0;width:1200px;text-align:center;font-family:'Josefin Sans',sans-serif;font-weight:700;font-size:23px;line-height:31px;color:var(--ink)}
.counter{top:1872px;font-family:'Josefin Sans',sans-serif;font-weight:700;font-size:58px;color:var(--orange)}
.user-icon{position:absolute;left:316px;top:1882px}
.savings-note{top:2028px;left:0;width:1200px;text-align:center;font-weight:700;font-size:17px;line-height:24px;color:var(--slate)}

.search{top:2111px;left:405px;width:390px;height:41px;border:2px solid var(--teal-light);display:flex}
.search-field{flex:1;font-size:15px;color:var(--teal-light);padding:11px 20px;font-weight:700;letter-spacing:.5px}
.search-btn{width:50px;border-left:2px solid var(--teal-light);display:flex;align-items:center;justify-content:center}

/* price table */
.price-table{top:2180px;left:147px;width:908px;height:430px;border-bottom:2px solid var(--rule)}
.price-head{display:flex;height:52px;border-bottom:1px solid var(--rule);font-size:17px;letter-spacing:1px;color:var(--grey);font-weight:700}
.price-head div{padding:26px 0 0 33px;border-right:2px solid var(--rule)}
.price-head div:last-child{border-right:none}
.scrollbar{position:absolute;right:0;top:53px;width:12px;height:376px;background:#f0f0f0}
.scrollbar::before{content:"";position:absolute;top:0;left:0;width:12px;height:18px;background:#9a9a9a}
.price-row{position:absolute;left:0;width:896px;height:85px;border-bottom:3px solid var(--teal-light)}
.price-row .name{position:absolute;left:33px;top:40px;font-size:13px;font-weight:700;line-height:15px}
.price-row .price{position:absolute;left:336px;top:46px;font-size:17px;font-weight:700}
.price-row .card{position:absolute;left:643px;top:46px;font-size:17px;font-weight:700}
.price-row .card small{font-size:8px;margin-left:10px;letter-spacing:.3px}

/* faq */
.faq-title{top:2754px;left:0;width:1200px;text-align:center;font-size:41px;font-weight:700;color:var(--slate)}
.faq-item{position:absolute;top:2884px;width:250px}
.faq-item h3{font-style:italic;font-weight:400;font-size:18px;line-height:23px;color:var(--ink);margin-bottom:10px}
.faq-item p{font-size:11px;line-height:15px;color:var(--grey)}
.faq-arrow{position:absolute;top:2948px}

/* footer */
.site-footer{position:absolute;left:0;top:3136px;width:1200px;height:155px;background:var(--footer);color:var(--white);font-weight:700}
.foot-head{position:absolute;top:36px;font-size:15px}
.foot-links{position:absolute;top:74px;font-size:15px;display:flex;gap:28px}
.social{position:absolute;left:990px;width:16px;height:16px;border-radius:50%;background:var(--white)}
</style>
</head>
<body>

<div class="deco" role="img" aria-label="Decorative teal pill and capsule pattern" style="left:0;top:0;width:320px;height:155px;border-radius:0 0 60px 0"></div>
<nav class="site-nav">
  <a href="#">HOME</a><a href="#">GET CARD</a><a href="#">PHARMACIES</a><a href="#">DRUG PRICING</a><a href="#">BLOG</a><a href="#" style="margin-right:0">CONTACT</a>
</nav>

<header>
  <div class="abs brand-dot"></div>
  <h1 class="abs hero-title">BRIGHTLEAF RX PASS</h1>
  <p class="abs hero-sub">Free Prescription&nbsp; Assistance Program</p>
  <a class="btn" href="#" style="top:443px">GET FREE CARD</a>
</header>

<div class="divider" style="top:540px;height:142px"></div>
<div class="deco" role="img" aria-label="Decorative pale teal pill pattern" style="left:910px;top:565px;width:290px;height:205px;border-radius:60px 0 0 60px"></div>
<div class="deco" role="img" aria-label="Decorative pale teal pill pattern" style="left:0;top:738px;width:230px;height:130px;border-radius:0 60px 60px 0"></div>

<section>
  <h2 class="section-title" style="top:742px"><span>Our Mission</span></h2>
  <p class="abs mission-lead">The Brightleaf Rx Pass is a FREE prescription assistance program that is available to everyone regardless of residency, age or income. This program is designed to assist those with no prescription coverage or for those whose prescription is not covered by insurance.</p>
  <p class="abs mission-body">This card will provide you with Rx medication savings of up to 75% at more than 60,000 pharmacies across the country including Corvell Pharmacy, Wayfield Drug, Rightway Care, Tallon Market, Valmore, Saferoad Foods, Grandly, Kessor Mart, Marlow's, Hollis Tate, Supra Green and many more.</p>
</section>

<div class="divider" style="top:1110px;height:142px"></div>

<section>
  <h2 class="section-title" style="top:1268px"><span>How To Use Your Card</span></h2>
  <div class="step-art" role="img" aria-label="Printer printing the card" style="left:192px;top:1410px;width:140px;height:162px"></div>
  <div class="step-art" role="img" aria-label="Hand presenting the card at the pharmacy counter" style="left:468px;top:1418px;width:262px;height:150px"></div>
  <div class="step-art" role="img" aria-label="Hand putting money into a purse" style="left:868px;top:1398px;width:140px;height:182px"></div>
  <p class="step-label" style="left:91px">Print Card</p>
  <p class="step-label" style="left:429px">Present Card At Pharmacy</p>
  <p class="step-label" style="left:768px">Save Money</p>
</section>

<section>
  <h2 class="abs savings-title">SAVINGS WITH<br>BRIGHTLEAF RX PASS</h2>
  <svg class="user-icon" width="30" height="48" viewBox="0 0 30 48" aria-hidden="true"><circle cx="15" cy="8" r="7.5" fill="#f26522"/><rect x="1" y="19" width="28" height="29" rx="5" fill="#f26522"/></svg>
  <p class="abs counter" style="left:364px">567</p>
  <div class="divider" style="top:1838px;height:148px"></div>
  <p class="abs counter" style="left:692px">$ 12345</p>
  <div class="deco" role="img" aria-label="Decorative pale teal pill pattern" style="left:1040px;top:1905px;width:160px;height:135px;opacity:.6;border-radius:50px 0 0 50px"></div>
  <p class="abs savings-note">Lorem ipsum dolor sit amet, no duo doming audire.<br>Ut congue posidonium mei, nominavi incorrupte mei et</p>

  <div class="abs search">
    <div class="search-field">SEARCH DRUG PRICES</div>
    <div class="search-btn"><svg width="20" height="20" viewBox="0 0 20 20" aria-hidden="true"><circle cx="8" cy="8" r="6" fill="none" stroke="#7fc8d8" stroke-width="2"/><line x1="12.5" y1="12.5" x2="18" y2="18" stroke="#7fc8d8" stroke-width="2.5"/></svg></div>
  </div>

  <div class="abs price-table">
    <div class="price-head">
      <div style="width:298px">PHARMACY</div>
      <div style="width:306px">PRICE</div>
      <div style="flex:1">CARD PRICES</div>
    </div>
    <div class="scrollbar"></div>
    <div class="price-row" style="top:52px"><p class="name">Lorem ipsum<br>dolor sit amet</p><p class="price">$ 100</p><p class="card">$ 50<small>SAVING 50 %</small></p></div>
    <div class="price-row" style="top:137px"><p class="name">Lorem ipsum<br>dolor sit amet</p><p class="price">$ 100</p><p class="card">$ 50<small>SAVING 50 %</small></p></div>
    <div class="price-row" style="top:222px"><p class="name">Lorem ipsum<br>dolor sit amet</p><p class="price">$ 100</p><p class="card">$ 50<small>SAVING 50 %</small></p></div>
    <div class="price-row" style="top:307px"><p class="name">Lorem ipsum<br>dolor sit amet</p><p class="price">$ 100</p><p class="card">$ 50<small>SAVING 50 %</small></p></div>
  </div>
  <a class="btn" href="#" style="top:2644px">GET FREE CARD</a>
</section>

<div class="deco" role="img" aria-label="Decorative pale teal pill pattern" style="left:0;top:2665px;width:175px;height:165px;opacity:.6;border-radius:0 50px 50px 0"></div>

<section>
  <h2 class="abs faq-title">Frequently Asked Questions</h2>
  <svg class="faq-arrow" style="left:146px" width="14" height="30" viewBox="0 0 14 30" aria-hidden="true"><polyline points="12,2 2,15 12,28" fill="none" stroke="#7fc8d8" stroke-width="2"/></svg>
  <div class="faq-item" style="left:180px">
    <h3>Do I have to pay at the time of service?</h3>
    <p>Yes, you pay the pharmacy once your prescription is filled. Participating pharmacies agree to charge only the discounted card price, not their usual full retail price.</p>
  </div>
  <div class="faq-item" style="left:474px">
    <h3>Can you tell me what my discount will be on my drugs?</h3>
    <p>Pricing can be provided by calling the Pharmacy &amp; Member Help Desk at Brightleaf Rx Pass, or it can be found on our website under drug pricing.</p>
  </div>
  <div class="faq-item" style="left:779px">
    <h3>Will I ever pay more using the card than I would without the card?</h3>
    <p>No, cardholders will always pay the lower of the card's contract price or the pharmacy's usual and customary price.</p>
  </div>
  <svg class="faq-arrow" style="left:1040px" width="14" height="30" viewBox="0 0 14 30" aria-hidden="true"><polyline points="2,2 12,15 2,28" fill="none" stroke="#7fc8d8" stroke-width="2"/></svg>
</section>

<footer class="site-footer">
  <p class="foot-head" style="left:193px">Services</p>
  <div class="foot-links" style="left:193px"><span>Get Card</span><span>Pharmacy Search</span><span>Drug Pricing</span></div>
  <p class="foot-head" style="left:654px">Quick Navigation</p>
  <div class="foot-links" style="left:654px;gap:44px"><span>Home</span><span>FAQ</span><span>Contact</span></div>
  <span class="social" style="top:38px"></span>
  <span class="social" style="top:76px"></span>
</footer>

</body>
</html>
```